Farhan Jewellers Stationary Contest

Pakistan’s largest Jewellery, Diamond and luxury watches store requires professional stationery. We have a long list of are trusted clients since 1959, our third generation has successfully maintained and sustained the legacy and excellence in the sector.

We require stationery template as part of this contest. The stationery can be double sided.

We prefer a design that makes use of some of the premium business stationery printing options, such as foil stamping, embossing/debossing, painted edges, spot UV etc (doesn't have to use all these options, only what you feel works, but we are looking for a design that stands out and is memorable and these nice touches have that effect.)

We want an eye catching, innovative, high end professional looking stationery for an out of box design that blends well with our new logo (attached). We want the design to be an out of box solution, you may use any element to compliment the logo. You may consider incorporating watermark etc, highlighting our products (Gold and Diamond Jewellery in addition to Luxury watches)

Company details are as follows;

Company name: Farhan Jewellers
Contact Person: Tariq Naveed
Designation: Business Development Consultant
Mobile: +92 333 815 6042
Email: tariqnaveed@mailvora.com
Website: www.farhanjewellers-pk.net

Target Market(s)

Matrimonial, Elite & Businesses class, Upmarket

Font styles to use
Other font styles liked:
• Designers choice

Colors

Designer to choose colors to be used in the design.

Requirements
Must have
• Look and feel: Upmarket, innovative, Modern, Professional, graceful, Elegant, designer stuff.
Nice to have
• Unique design

```html
<!DOCTYPE html>
<html lang="en">
<head>
<meta charset="utf-8">
<title>Farhan Jewellers – Business Card</title>
<link rel="stylesheet" href="https://fonts.googleapis.com/css2?family=Montserrat:wght@600&family=Poppins:wght@300;400&display=swap">
<style>
  :root {
    --backdrop: #1b1b1b;
    --card: #121212;
    --card-edge: #0a0a0a;
    --gold: #e8a824;
    --silver: #c9c9c9;
    --ink-light: #f1f1f1;
  }
  * { margin: 0; padding: 0; box-sizing: border-box; }
  html, body { width: 1200px; height: 900px; overflow: hidden; }
  body {
    background: radial-gradient(ellipse at 50% 40%, #2a2a2a 0%, var(--backdrop) 70%);
    font-family: "Poppins", Arial, sans-serif;
    position: relative;
  }
  .card {
    position: absolute;
    left: 280px;
    width: 640px;
    height: 366px;
    background: var(--card);
    border: 1px solid var(--card-edge);
    box-shadow: 0 18px 40px rgba(0,0,0,0.6);
  }
  .card--back { top: 60px; display: flex; align-items: center; justify-content: center; }
  .card--front { top: 474px; }

  .back-wordmark {
    font-family: "Montserrat", Arial, sans-serif;
    font-weight: 600;
    font-size: 24px;
    letter-spacing: 4px;
    color: var(--silver);
    text-transform: uppercase;
  }

  .brand {
    position: absolute;
    left: 44px;
    top: 150px;
    width: 250px;
    display: flex;
    align-items: center;
    gap: 10px;
  }
  .brand__dot {
    width: 14px; height: 14px; border-radius: 50%;
    background: var(--gold);
    flex: none;
  }
  .brand__name {
    font-family: "Montserrat", Arial, sans-serif;
    font-weight: 600;
    font-size: 19px;
    letter-spacing: 1px;
    color: var(--gold);
    text-transform: uppercase;
    white-space: nowrap;
  }

  .divider {
    position: absolute;
    left: 318px;
    top: 95px;
    width: 2px;
    height: 150px;
    background: var(--gold);
  }

  .contact {
    position: absolute;
    left: 345px;
    top: 112px;
  }
  .contact__name {
    font-family: "Montserrat", Arial, sans-serif;
    font-weight: 600;
    font-size: 20px;
    letter-spacing: 2px;
    color: var(--gold);
    text-transform: uppercase;
    line-height: 1.1;
  }
  .contact__role {
    font-size: 14px;
    font-weight: 400;
    letter-spacing: 0.8px;
    color: var(--ink-light);
    margin-bottom: 22px;
  }
  .contact__list { list-style: none; }
  .contact__item {
    display: flex;
    align-items: center;
    gap: 14px;
    font-size: 15px;
    font-weight: 300;
    color: var(--ink-light);
    line-height: 26px;
  }
  .contact__icon { width: 14px; height: 14px; flex: none; }
  .contact__highlight { color: var(--gold); }
</style>
</head>
<body>
  <section class="card card--back">
    <span class="back-wordmark">Farhan Jewellers</span>
  </section>

  <section class="card card--front">
    <div class="brand">
      <span class="brand__dot"></span>
      <span class="brand__name">Farhan Jewellers</span>
    </div>

    <div class="divider"></div>

    <div class="contact">
      <h1 class="contact__name">Tariq Naveed</h1>
      <p class="contact__role">Business Development Consultant</p>
      <ul class="contact__list">
        <li class="contact__item">
          <svg class="contact__icon" viewBox="0 0 16 16"><path fill="#e8a824" d="M3.6 1.5l2.2 2.6-1.3 1.6c.9 2.2 2.8 4.1 5 5l1.6-1.3 2.6 2.2-1.4 2.6C6.7 13.8 2.2 9.3 1 3z"/></svg>
          <span>+92 333 815 6042</span>
        </li>
        <li class="contact__item">
          <svg class="contact__icon" viewBox="0 0 16 16"><rect x="1" y="3" width="14" height="10" fill="#e8a824"/><path d="M1 3l7 6 7-6" fill="none" stroke="#121212" stroke-width="1.3"/></svg>
          <span>tariqnaveed@mailvora.com</span>
        </li>
        <li class="contact__item">
          <svg class="contact__icon" viewBox="0 0 16 16" fill="none" stroke="#e8a824" stroke-width="1.3"><circle cx="8" cy="8" r="6.5"/><ellipse cx="8" cy="8" rx="2.8" ry="6.5"/><path d="M1.5 8h13M2.5 4.8h11M2.5 11.2h11"/></svg>
          <span>www.<span class="contact__highlight">farhanjewellers-pk</span>.net</span>
        </li>
      </ul>
    </div>
  </section>
</body>
</html>
```